Family history tech product tailored for moms needs banner ads

kinloam.example is launching next week and we've partnered with an ad group that will be launching a campaign on school district websites that will be pushed to 250k moms of school age children.

We're launching a $199 product that shows you more about who you are through your family's history. We connect people wanting to learn more about themselves with expert researcher/genealogist who will uncover their past and find the stories of their ancestors.

See branding guidelines below as well as the landing page we're designing where these ads will take you.

Here is the landing page design:
https://chatbox-files.example/X839KQ2M1-G72P4TTR8-kf4e1mzq90

Target Market(s)

Mom's of kids in elementary and middle school.

Persona:
Mom, 38 years old, 2 kids (age 6 and 8)
Lives in Dallas, drives a 2016 Vormak Ridgel
She and husband met in college. She was a nurse, but she stopped working to be a full-time mom
Husband is in financial consulting, household income of $140,000
When kids at school, she runs errands, works out, meets up with girlfriends for coffee
She shops at Sorvanta, has active hobbies
She is always busy, there’s not enough time for her family; she is worried that her kids may become distant because of how busy the family is
She values time with family most, soccer weekends, financial stability, college for the kids
Wants to connect more with the kids and the family to increase the bond, and she thinking having more context for the family will help them bond around a common history
Her objections to Kinloam are lack of trust in a new service, time it will cost her to get the info she wants to achieve her goals

Industry/Entity Type

Startup

Font styles to use
Other font styles liked:
• follow style guide

Requirements
Must have
• Must follow the design pattern in our branding guide.
• https://www.filecrate.example/s/kqm4tnw819zpxa/Screenshot%202016-11-30%2013.39.48.png?dl=0
Nice to have
• Good copy, I'm less worried about that though. We can work together on that.
Should not have
• Stock imagery that sucks. I'm really opposed to anything that looks like it is from the 2001 - 2011

```html
<!DOCTYPE html>
<html lang="en">
<head>
<meta charset="utf-8">
<title>Kinloam — Everyone has a story. Find yours.</title>
<link rel="stylesheet" href="https://fonts.googleapis.com/css2?family=Open+Sans:wght@400;600;700&display=swap">
<style>
  :root {
    --canvas: #ffffff;
    --backdrop-light: #f4f9fe;
    --backdrop-tint: #dcecfb;
    --slate: #3d5670;
    --teal: #14979f;
    --button-navy: #243545;
    --band-aqua: #45c6d3;
    --band-shadow: #d3d6d8;
    --brand-blue: #3a9bf5;
    --skin-light: #f6d3c0;
    --skin-deep: #e6a98f;
    --white: #ffffff;
  }

  * { box-sizing: border-box; margin: 0; padding: 0; }

  html, body {
    width: 1200px;
    height: 500px;
    overflow: hidden;
    background: var(--canvas);
  }

  .banner {
    position: relative;
    width: 1200px;
    height: 500px;
    overflow: hidden;
    background: var(--canvas);
    font-family: "Open Sans", Arial, sans-serif;
  }

  .banner__backdrop {
    position: absolute;
    inset: 0;
    background:
      radial-gradient(ellipse 420px 260px at 230px 240px, var(--backdrop-tint) 0%, rgba(220,236,251,0) 100%),
      radial-gradient(ellipse 360px 280px at 960px 260px, var(--backdrop-tint) 0%, rgba(220,236,251,0) 100%),
      linear-gradient(135deg, var(--backdrop-light) 0%, var(--canvas) 55%, var(--backdrop-light) 100%);
  }

  .headline {
    position: absolute;
    left: 44px;
    top: 134px;
  }

  .headline__lead {
    display: block;
    margin-left: 26px;
    font-size: 47px;
    font-weight: 700;
    line-height: 1;
    letter-spacing: -0.5px;
    color: var(--slate);
  }

  .headline__call {
    display: block;
    margin-top: 10px;
    font-size: 92px;
    font-weight: 700;
    line-height: 1;
    letter-spacing: -2px;
    color: var(--teal);
  }

  .cta-button {
    position: absolute;
    left: 122px;
    top: 344px;
    width: 384px;
    height: 92px;
    display: flex;
    align-items: center;
    justify-content: center;
    background: var(--button-navy);
    color: var(--white);
    font-size: 52px;
    font-weight: 700;
    letter-spacing: -0.5px;
    text-decoration: none;
  }

  .tagline-band__shadow {
    position: absolute;
    left: 612px;
    top: 8px;
    width: 76px;
    height: 456px;
    background: var(--band-shadow);
  }

  .tagline-band {
    position: absolute;
    left: 602px;
    top: 0;
    width: 76px;
    height: 474px;
    background: var(--band-aqua);
  }

  .tagline-band__text {
    position: absolute;
    left: 50%;
    top: 212px;
    transform: translate(-50%, -50%) rotate(-90deg);
    white-space: nowrap;
    font-size: 28px;
    font-weight: 400;
    letter-spacing: 6.5px;
    color: var(--white);
  }

  .hands-photo {
    position: absolute;
    left: 768px;
    top: 140px;
    width: 284px;
    height: 360px;
    border-radius: 40px 40px 0 0;
    background: radial-gradient(ellipse at 50% 40%, var(--skin-light) 0%, var(--skin-deep) 100%);
  }

  .brand {
    position: absolute;
    left: 1088px;
    top: 36px;
    transform: translateX(-50%);
    display: flex;
    flex-direction: column;
    align-items: center;
    gap: 10px;
  }

  .brand__dot {
    width: 56px;
    height: 56px;
    border-radius: 50%;
    background: var(--brand-blue);
  }

  .brand__name {
    font-size: 34px;
    font-weight: 700;
    line-height: 1;
    color: var(--brand-blue);
    white-space: nowrap;
  }
</style>
</head>
<body>
  <main class="banner">
    <div class="banner__backdrop" role="img" aria-label="Soft light-blue background of diagonal rounded stripes"></div>

    <h1 class="headline">
      <span class="headline__lead">Everyone has a story…</span>
      <span class="headline__call">Find yours.</span>
    </h1>

    <a class="cta-button" href="https://kinloam.example">Learn More</a>

    <div class="tagline-band__shadow"></div>
    <div class="tagline-band">
      <p class="tagline-band__text">Yourself, Discovered.</p>
    </div>

    <div class="hands-photo" role="img" aria-label="Photo of a child's hand pressed against an adult's open hand, fingers spread"></div>

    <div class="brand">
      <span class="brand__dot"></span>
      <span class="brand__name">Kinloam</span>
    </div>
  </main>
</body>
</html>
```